Construction Company

I'm a new construction company called Tembrik Construction. I want my card to look simple and clean. I have provided a sample of what I want the front to look like (Tembrik_Card.jpeg) and a back ground for the back of the (Tembrik_Card_Background.jpeg) - the background can be faded so my name and other information is more prominent.
Construction

```html
<!DOCTYPE html>
<html lang="en">
<head>
<meta charset="utf-8">
<title>Tembrik Construction – Business Card</title>
<link rel="stylesheet" href="https://fonts.googleapis.com/css2?family=Lato:wght@400;700;900&display=swap">
<style>
  :root {
    --stage: #2b2b2b;
    --olive-light: #4b4627;
    --olive-dark: #2f2c19;
    --orange: #ef9300;
    --ink: #1c1c1c;
    --paper: #ffffff;
    --plan-tone: #eeeeee;
    --plan-tone-edge: #f8f8f8;
  }
  * { box-sizing: border-box; margin: 0; padding: 0; }
  html, body {
    width: 1200px;
    height: 997px;
    overflow: hidden;
    background: var(--stage);
    font-family: "Lato", sans-serif;
  }
  .stage {
    width: 1200px;
    height: 997px;
    display: flex;
    flex-direction: column;
    align-items: center;
    justify-content: center;
    gap: 60px;
  }
  .card {
    width: 700px;
    height: 400px;
    border-radius: 28px;
    position: relative;
    overflow: hidden;
  }
  /* Front */
  .card--front {
    background: linear-gradient(135deg, var(--olive-light), var(--olive-dark));
    display: flex;
    align-items: center;
    justify-content: center;
  }
  .brand-name {
    color: var(--orange);
    font-weight: 700;
    font-size: 64px;
    letter-spacing: 2px;
    line-height: 1;
  }
  /* Back */
  .card--back {
    background: var(--paper);
  }
  .plan-area {
    position: absolute;
    left: 90px;
    top: 40px;
    width: 520px;
    height: 320px;
    background: radial-gradient(ellipse at center, var(--plan-tone), var(--plan-tone-edge));
    opacity: 0.7;
  }
  .contact-block {
    position: absolute;
    left: 0;
    right: 0;
    top: 150px;
    display: flex;
    align-items: center;
    justify-content: center;
    gap: 22px;
  }
  .identity { text-align: right; }
  .person-name {
    color: var(--orange);
    font-weight: 900;
    font-size: 24px;
    letter-spacing: 0.5px;
  }
  .person-role {
    color: var(--ink);
    font-weight: 700;
    font-size: 16px;
    margin-top: 2px;
  }
  .divider {
    width: 4px;
    height: 70px;
    background: var(--orange);
  }
  .details {
    color: var(--ink);
    font-weight: 700;
    font-size: 16px;
    line-height: 1.7;
  }
</style>
</head>
<body>
  <main class="stage">
    <section class="card card--front">
      <h1 class="brand-name">Tembrik Construction</h1>
    </section>

    <section class="card card--back">
      <div class="plan-area" role="img" aria-label="Faded architectural floor plan of a house as card background"></div>
      <div class="contact-block">
        <div class="identity">
          <p class="person-name">DANIEL HART</p>
          <p class="person-role">Owner / Founder</p>
        </div>
        <span class="divider"></span>
        <div class="details">
          <p class="phone">(555) 214-6803</p>
          <p class="email">daniel@tembrikconstruction.com</p>
        </div>
      </div>
    </section>
  </main>
</body>
</html>
```